Brightmoor Senior Living Marketing Brochure, Covid-19 Brochure, Introduction to our manager

We are a Senior Living Community that services Assisted living and memory care. We have a lot of New programs for Activities, Food recipes, therapy, family and resident interaction , covid free, and want to introduce this to the community and existing family members.

Target Market(s)

La Jolla and San Diego for Brightmoor Senior Living and Memory Care of La Jolla and For Brightmoor Senior Living and Memory Care of Tarzana , San Fernando valley, tarzana, Encino , Woodland Hills Sherman oaks

Industry/Entity Type

Assisted Living

Font styles to use

Colors
a54499
f7f3f9
ffffff
fece3e
ffc214

Requirements
Must have
• Product names for our marketing brochure , facility images per location

```html
<!DOCTYPE html>
<html lang="en">
<head>
<meta charset="utf-8">
<title>Brightmoor Senior Living Marketing Brochure</title>
<link href="https://fonts.googleapis.com/css2?family=Montserrat:wght@300;400;500;600&family=Playfair+Display:wght@700&display=swap" rel="stylesheet">
<style>
:root{
  --purple:#a54499;
  --purple-deep:#8e2f7c;
  --lilac:#f7f3f9;
  --white:#ffffff;
  --yellow:#fece3e;
  --gold:#ffc214;
  --ink:#4a4450;
  --board:#ffffff;
}
*{margin:0;padding:0;box-sizing:border-box}
html,body{width:769px;height:1200px;overflow:hidden;background:var(--board)}
body{position:relative;font-family:"Montserrat",sans-serif;color:var(--ink)}
.label{position:absolute;left:0;width:769px;text-align:center;font-weight:300;font-size:34px;letter-spacing:6px;color:#3a3a3a}
.label-outside{top:58px}
.label-inside{top:626px}
.spread{position:absolute;left:31px;width:707px;background:var(--white);box-shadow:0 2px 10px rgba(0,0,0,.18);overflow:hidden}
.spread-outside{top:128px;height:422px}
.spread-inside{top:696px;height:482px}
.abs{position:absolute}
.serif{font-family:"Playfair Display",serif;font-weight:700}
/* outside */
.cover-block{left:20px;top:14px;width:330px;height:376px;background:var(--yellow)}
.quote-mark{left:44px;top:14px;font-size:92px;line-height:1;color:var(--purple)}
.cover-title{left:44px;top:100px;width:250px;font-size:40px;line-height:1.1;color:var(--purple)}
.cover-info{left:30px;top:288px;width:300px;height:62px;background:var(--white);display:flex;gap:14px;padding:9px 12px;font-size:7.5px;line-height:1.45}
.cover-info div{flex:1}
.cover-info b{color:var(--purple);font-weight:600}
.web-strip{left:20px;top:358px;width:330px;height:34px;background:var(--purple);color:var(--white);font-family:"Playfair Display",serif;font-weight:700;font-size:16px;line-height:34px;padding-left:24px}
.brand{right:26px;top:18px;display:flex;align-items:center;gap:6px;color:var(--purple);font-family:"Playfair Display",serif;font-weight:700;font-size:20px;letter-spacing:1px}
.brand .dot{width:12px;height:12px;border-radius:50%;background:var(--purple)}
.brand-tag{right:26px;top:48px;background:var(--purple);color:var(--white);font-size:8px;padding:4px 10px}
.photo-outside{left:353px;top:78px;width:354px;height:262px;background:linear-gradient(135deg,#c9c2a6,#8f9a7a 55%,#d8cbb4)}
.lux-box{left:455px;top:228px;width:238px;height:178px;background:var(--purple);padding:16px 16px}
.lux-box h2{font-size:25px;line-height:1.15;color:var(--white);margin-bottom:12px}
.lux-box li{list-style:none;color:var(--yellow);font-size:7.5px;line-height:1.4;margin-bottom:6px;padding-left:10px;position:relative}
.lux-box li:before{content:"";position:absolute;left:0;top:3px;width:5px;height:5px;background:var(--yellow)}
/* inside */
.salon-title{left:22px;top:22px;font-size:19px;line-height:1.2;color:var(--purple);width:220px}
.list{font-size:7.5px;line-height:1.55}
.list li{list-style:none;padding-left:9px;position:relative}
.list li:before{content:"";position:absolute;left:0;top:4px;width:4px;height:4px;border-radius:50%;background:var(--purple)}
.list-a{left:22px;top:74px;width:160px}
.list-b{left:196px;top:74px;width:150px}
.feature-box{left:18px;top:152px;width:172px;height:150px;border:1px solid var(--purple);padding:8px 8px}
.list-c{left:196px;top:152px;width:150px}
.note{left:22px;top:318px;width:320px;font-size:7px;line-height:1.4;color:var(--purple-deep);background:var(--lilac);padding:3px 4px}
.photo-inside{left:353px;top:14px;width:340px;height:318px;background:linear-gradient(160deg,#e9e4de,#c8b6a5 55%,#9d8b7d)}
.band{left:0;top:340px;width:707px;height:142px;background:var(--purple);display:flex;padding:14px 14px;gap:14px}
.band-col{flex:1;color:var(--white)}
.band-col h3{font-family:"Playfair Display",serif;font-weight:700;font-size:17px;line-height:1.05;margin-bottom:8px}
.band-col p{font-size:6.8px;line-height:1.45;opacity:.92}
.stat{display:flex;flex-direction:column;gap:6px}
.stat-card{background:var(--white);padding:6px 8px;display:flex;align-items:flex-end;justify-content:space-between}
.stat-card b{font-family:"Playfair Display",serif;font-size:24px;color:var(--purple)}
</style>
</head>
<body>
<div class="label label-outside">OUTSIDE</div>

<section class="spread spread-outside">
  <div class="abs cover-block"></div>
  <div class="abs quote-mark serif">&ldquo;</div>
  <h1 class="abs cover-title serif">Creating A Healthy Living Environment</h1>
  <div class="abs cover-info">
    <div><b>Brightmoor Senior Living</b><br>8120 Coastline Avenue<br>Harbor Point, Seacliff County<br>(555) 014-2290</div>
    <div><b>Senior Residence</b><br>Harbor Point, Seacliff County<br>Care, comfort and<br>community every day</div>
  </div>
  <div class="abs web-strip">brightmoorseniorliving.com</div>

  <div class="abs photo-outside" role="img" aria-label="Photo of a senior resident smiling with a younger caregiver outdoors"></div>
  <div class="abs brand"><span class="dot"></span>BRIGHTMOOR</div>
  <div class="abs brand-tag">Creating A Healthy Living Environment</div>
  <div class="abs lux-box">
    <h2 class="serif">Luxurious Senior Living</h2>
    <ul>
      <li>Over 100 residents enjoy assisted living and memory care.</li>
      <li>Daily activities, fresh meals and therapy, kept safe and Covid free.</li>
    </ul>
  </div>
</section>

<div class="label label-inside">INSIDE</div>

<section class="spread spread-inside">
  <h2 class="abs salon-title serif">Salon for nails, hair and massages :</h2>
  <ul class="abs list list-a">
    <li>Chef-prepared meals served daily</li>
    <li>Weekly fitness and yoga</li>
    <li>Medication management</li>
    <li>Housekeeping and laundry</li>
    <li>Transportation to appointments</li>
  </ul>
  <ul class="abs list list-b">
    <li>Garden walks</li>
    <li>Art and music programs</li>
    <li>Social hour with friends</li>
    <li>Family visits welcome</li>
    <li>Movie nights</li>
  </ul>
  <div class="abs feature-box">
    <ul class="list">
      <li>Licensed nurses on site around the clock</li>
      <li>Memory care with gentle daily routines</li>
      <li>New recipes from our kitchen team</li>
      <li>Physical and speech therapy on site</li>
      <li>Private suites with modern comforts and safety features</li>
      <li>Meet our manager, here to help every family</li>
    </ul>
  </div>
  <ul class="abs list list-c">
    <li>Wi-Fi and video calls</li>
    <li>Spa and wellness</li>
    <li>Scheduled outings to local parks and shops each week</li>
    <li>Library nook</li>
    <li>Clean, safe spaces with daily health checks for all residents and staff members</li>
    <li>Pet friendly</li>
  </ul>
  <p class="abs note">Brightmoor Senior Living is welcoming new residents at both communities.</p>

  <div class="abs photo-inside" role="img" aria-label="Photo of a smiling senior couple embracing"></div>

  <div class="abs band">
    <div class="band-col"><h3>Living<br>Relive</h3><p>Fresh activities each day help residents stay active and engaged.</p></div>
    <div class="band-col"><h3>Connect<br>Reconnect</h3><p>Family and resident events bring loved ones closer together.</p></div>
    <div class="band-col"><h3>Lightbulb<br>Reinspire</h3><p>New programs in art, music and therapy spark daily joy.</p></div>
    <div class="band-col"><h3>Family<br>Members</h3><p>Regular updates keep every family informed and involved.</p></div>
    <div class="band-col stat">
      <div class="stat-card"><b>40%</b>
        <svg width="34" height="26" viewBox="0 0 34 26"><rect x="2" y="16" width="6" height="10" fill="#a54499"/><rect x="11" y="10" width="6" height="16" fill="#a54499"/><rect x="20" y="5" width="6" height="21" fill="#a54499"/><rect x="28" y="0" width="6" height="26" fill="#ffc214"/></svg>
      </div>
      <p>More activity hours this year for every resident.</p>
    </div>
  </div>
</section>
</body>
</html>
```